RZ Advisory Business Cards - High End AV / Low Voltage Company

We are low voltage AV company that specializes in high end clients on the residential side and larger businesses on the commercial side. We want something modern, tech looking but also something that is extremely professional looking. We have uploaded our logos and postcards we already have in the field. Along with a picture of one of our wrapped vans. Our website is at www.rzadvisory.example and our primary colors are the orange, green, grey and blue all military color finishes.

We are interesting in the slogans "Matching You with the Ideal Equipment" or "Guiding the Harborlands in Tech"

Target Market(s)

We focus on 70% Commercial and 30% Residential Customers

Industry/Entity Type

Low Voltage, AV Company

Contact Information for Business Card

Name - Dorian Fenwick, Title - Owner, Office Phone - 555-402-7163, Mobile Phone - 555-718-3094, E-Mail - t@rzadvisory.example, Website: www.rzadvisory.example

Font styles to use
Sans Serif

Requirements
Must have
• Must have Name, Title, Work Phone & Mobile, Website and Logo.
Nice to have
• We want something that will impress our higher end clients with a great logo
Should not have
• Too traditional or plain.

```html
<!DOCTYPE html>
<html lang="en">
<head>
<meta charset="UTF-8">
<title>RZ Advisory — Business Card</title>
<link rel="stylesheet" href="https://fonts.googleapis.com/css2?family=Libre+Franklin:wght@400;500;700&display=swap">
<style>
  :root {
    --brand-orange: #e8673a;
    --ink: #1c1c1c;
    --rule: #9a9a9a;
    --card: #ffffff;
    --backdrop: #e9e9e9;
  }
  * { box-sizing: border-box; margin: 0; padding: 0; }
  html, body {
    width: 1200px;
    height: 800px;
    overflow: hidden;
    background: var(--backdrop);
    font-family: "Libre Franklin", Arial, sans-serif;
  }
  .card {
    position: absolute;
    left: 142px;
    top: 125px;
    width: 915px;
    height: 550px;
    background: var(--card);
    overflow: hidden;
  }
  .card__band {
    position: absolute;
    left: 0; right: 0; bottom: 0;
    height: 12px;
    background: var(--brand-orange);
  }
  .brand {
    position: absolute;
    left: 78px;
    top: 190px;
    display: flex;
    align-items: center;
    gap: 14px;
  }
  .brand__dot {
    width: 34px;
    height: 34px;
    border-radius: 50%;
    background: var(--brand-orange);
  }
  .brand__name {
    color: var(--brand-orange);
    font-weight: 700;
    font-size: 44px;
    letter-spacing: 0.5px;
    line-height: 1;
  }
  .tagline {
    position: absolute;
    left: 443px;
    top: 208px;
    color: var(--brand-orange);
    font-weight: 700;
    font-size: 24px;
    line-height: 30px;
    letter-spacing: 0.4px;
    text-transform: uppercase;
  }
  .contact {
    position: absolute;
    left: 0;
    top: 442px;
    width: 100%;
    height: 66px;
  }
  .person {
    position: absolute;
    right: calc(915px - 357px);
    top: 8px;
    text-align: right;
  }
  .person__name {
    color: var(--brand-orange);
    font-weight: 700;
    font-size: 24px;
    letter-spacing: 0.3px;
    text-transform: uppercase;
    line-height: 28px;
  }
  .person__title {
    color: var(--ink);
    font-size: 17px;
    line-height: 22px;
  }
  .divider {
    position: absolute;
    top: 0;
    width: 1px;
    height: 66px;
    background: var(--rule);
  }
  .divider--first { left: 378px; }
  .divider--second { left: 583px; }
  .detail-list {
    position: absolute;
    top: 8px;
    list-style: none;
  }
  .detail-list--phones { left: 396px; }
  .detail-list--web { left: 598px; }
  .detail {
    display: flex;
    align-items: center;
    gap: 12px;
    height: 29px;
    color: var(--ink);
    font-size: 20px;
    font-weight: 500;
  }
  .detail__icon {
    width: 18px;
    height: 18px;
    flex: none;
    stroke: var(--brand-orange);
    fill: none;
    stroke-width: 1.8;
    stroke-linecap: round;
    stroke-linejoin: round;
  }
</style>
</head>
<body>
  <main class="card">
    <div class="brand">
      <span class="brand__dot"></span>
      <span class="brand__name">RZ Advisory</span>
    </div>

    <p class="tagline">Matching you with the<br>ideal equipment</p>

    <section class="contact">
      <div class="person">
        <p class="person__name">Dorian Fenwick</p>
        <p class="person__title">Owner</p>
      </div>

      <span class="divider divider--first"></span>

      <ul class="detail-list detail-list--phones">
        <li class="detail">
          <svg class="detail__icon" viewBox="0 0 24 24" aria-hidden="true"><path d="M5 3h4l2 5-2.5 1.5a11 11 0 0 0 6 6L16 13l5 2v4a2 2 0 0 1-2 2A16 16 0 0 1 3 5a2 2 0 0 1 2-2z"/><path d="M15 3a6 6 0 0 1 6 6M15 7a2 2 0 0 1 2 2"/></svg>
          <span>555-402-7163</span>
        </li>
        <li class="detail">
          <svg class="detail__icon" viewBox="0 0 24 24" aria-hidden="true"><rect x="7" y="2" width="10" height="20" rx="2"/><path d="M11 18h2"/></svg>
          <span>555-718-3094</span>
        </li>
      </ul>

      <span class="divider divider--second"></span>

      <ul class="detail-list detail-list--web">
        <li class="detail">
          <svg class="detail__icon" viewBox="0 0 24 24" aria-hidden="true"><rect x="3" y="5" width="18" height="14" rx="1"/><path d="M3 7l9 6 9-6"/></svg>
          <span>t@rzadvisory.example</span>
        </li>
        <li class="detail">
          <svg class="detail__icon" viewBox="0 0 24 24" aria-hidden="true"><circle cx="12" cy="12" r="9"/><path d="M3 12h18M12 3c3 3 3 15 0 18M12 3c-3 3-3 15 0 18"/></svg>
          <span>www.rzadvisory.example</span>
        </li>
      </ul>
    </section>

    <div class="card__band"></div>
  </main>
</body>
</html>
```